New Company Business Card design

Looking for a corporate looking business card utilising my new logo design - the logo i would like embossed as one option and flat as another - simplistic but stylish - less is more - we are an import export business launching into the market - i would like a couple of options as main background - Grey or Black

```html
<!DOCTYPE html>
<html lang="en">
<head>
<meta charset="utf-8">
<title>Meridian Trade Partners – Business Cards</title>
<link rel="stylesheet" href="https://fonts.googleapis.com/css2?family=Roboto:wght@400;500&display=swap">
<style>
  :root {
    --backdrop: #021a2a;
    --card-white: #ffffff;
    --charcoal: #414042;
    --brand-blue: #0e6ca8;
    --silver: #e2e3e5;
    --ink: #333335;
    --muted: #6d6e71;
    --on-dark: #ffffff;
  }
  * { margin: 0; padding: 0; box-sizing: border-box; }
  html, body {
    width: 1200px; height: 1200px; overflow: hidden;
    background: var(--backdrop);
    font-family: "Roboto", Arial, sans-serif;
  }
  .stage {
    position: relative;
    width: 1500px; height: 1500px;
    transform: scale(0.8); transform-origin: 0 0;
  }
  .card {
    position: absolute;
    width: 490px; height: 853px;
    background: var(--card-white);
    overflow: hidden;
    box-shadow: 0 2px 6px rgba(0,0,0,0.45);
  }
  .card--front { left: 200px; top: 108px; }
  .card--back  { left: 870px; top: 561px; }

  .card__decor {
    position: absolute; left: 0; right: 0; top: 260px; height: 370px;
    background: linear-gradient(to bottom,
      var(--card-white) 0%, var(--silver) 30%,
      var(--brand-blue) 45%, var(--brand-blue) 62%,
      var(--charcoal) 100%);
  }
  .card__base {
    position: absolute; left: 0; right: 0; top: 630px; bottom: 0;
    background: var(--charcoal);
  }

  .brand {
    position: absolute; left: 0; right: 0; top: 40px;
    display: flex; flex-direction: column; align-items: center;
  }
  .brand__dot {
    width: 110px; height: 110px; border-radius: 50%;
    background: var(--brand-blue);
    margin-bottom: 24px;
  }
  .brand__name {
    font-size: 27px; font-weight: 500; letter-spacing: 1.5px;
    line-height: 1; color: var(--brand-blue); white-space: nowrap;
  }
  .brand__tagline {
    margin-top: 12px;
    font-size: 10.5px; letter-spacing: 2.6px; color: var(--muted);
    text-transform: uppercase; white-space: nowrap;
  }

  .holder {
    position: absolute; left: 0; right: 0; top: 285px;
    text-align: center;
  }
  .holder__name {
    font-size: 40px; font-weight: 400; letter-spacing: 1px; color: var(--ink);
    line-height: 1;
  }
  .holder__name .initial { color: var(--brand-blue); }
  .holder__role { margin-top: 10px; font-size: 21px; color: #4a4a4c; }

  .contact {
    position: absolute; left: 0; right: 0;
    text-align: center; color: var(--on-dark);
    font-size: 20px; letter-spacing: 1px; line-height: 26px;
    font-style: normal; white-space: nowrap;
  }
  .contact--address { top: 629px; }
  .contact--lines { top: 737px; }
  .contact--web { top: 790px; }
</style>
</head>
<body>
<div class="stage">

  <section class="card card--front">
    <div class="card__decor" role="img" aria-label="Flowing blue, grey and silver wave decoration"></div>
    <div class="card__base"></div>

    <header class="brand">
      <div class="brand__dot"></div>
      <div class="brand__name">MERIDIAN TRADE PARTNERS</div>
      <div class="brand__tagline">Worldwide supply for regional markets</div>
    </header>

    <div class="holder">
      <h1 class="holder__name"><span class="initial">J</span>OHN <span class="initial">D</span>OE</h1>
      <p class="holder__role">Director</p>
    </div>

    <address class="contact contact--address">
      Dummy Street<br>Dummy City, Dummy Country
    </address>
    <p class="contact contact--lines">
      +63 900 555 0142<br>
      john@meridiantradepartners.com<br>
      www.meridiantradepartners.com
    </p>
  </section>

  <section class="card card--back">
    <div class="card__decor" role="img" aria-label="Flowing blue, grey and silver wave decoration"></div>
    <div class="card__base"></div>

    <header class="brand">
      <div class="brand__dot"></div>
      <div class="brand__name">MERIDIAN TRADE PARTNERS</div>
      <div class="brand__tagline">Worldwide supply for regional markets</div>
    </header>

    <p class="contact contact--web">www.meridiantradepartners.com</p>
  </section>

</div>
</body>
</html>
```